Brookvale Systems, Water conservation business that needs a stand out, eye catching Facebook Design.

I am look for a pro to take the Logo I have, and apply some pics I will supply or there own ideas, and create a Facebook page design, that people will want to continue looking at and gain interest in wanting to see more of what we offer.

```html
<!DOCTYPE html>
<html lang="en">
<head>
<meta charset="UTF-8">
<title>Brookvale Systems – Water Conservation for Businesses</title>
<link href="https://fonts.googleapis.com/css2?family=Poppins:wght@600;700;800&family=Montserrat:wght@700&display=swap" rel="stylesheet">
<style>
  :root {
    --bg-top: #6aaed0;
    --bg-bottom: #3fe3bd;
    --card: #f2f2f2;
    --green: #0f9a3d;
    --blue: #1e8fd6;
    --white: #ffffff;
    --sky-top: #1d6fd0;
    --sky-mid: #8cc3ea;
    --field: #4fae3a;
    --field-dark: #2f7d2a;
  }
  * { margin: 0; padding: 0; box-sizing: border-box; }
  html, body { width: 1200px; height: 1200px; overflow: hidden; }
  body {
    background: linear-gradient(180deg, var(--bg-top) 0%, var(--bg-bottom) 100%);
    font-family: "Poppins", sans-serif;
    position: relative;
  }
  .post {
    position: absolute;
    left: 73px; top: 73px;
    width: 1054px; height: 1054px;
    background: var(--card);
    box-shadow: 0 10px 40px rgba(0,0,0,0.35);
    overflow: hidden;
  }
  .brand {
    position: absolute;
    left: 84px; top: 108px;
    display: flex; align-items: center; gap: 14px;
  }
  .brand-mark {
    width: 44px; height: 44px; border-radius: 50%;
    background: var(--blue);
  }
  .brand-name {
    font-family: "Poppins", sans-serif;
    font-weight: 700;
    font-size: 34px;
    color: var(--green);
    letter-spacing: 0.5px;
  }
  .dots {
    position: absolute;
    display: grid;
    grid-template-columns: repeat(3, 17px);
    gap: 20px;
  }
  .dots span { width: 17px; height: 17px; border-radius: 50%; }
  .dots-top { left: 925px; top: 44px; }
  .dots-top span { background: var(--blue); }
  .dots-bottom { left: 36px; top: 934px; }
  .dots-bottom span { background: var(--green); }
  .hero { position: absolute; left: 0; top: 185px; width: 1054px; height: 690px; }
  .headline {
    position: absolute;
    right: 36px; top: 248px;
    text-align: right;
    color: var(--white);
    font-weight: 800;
    font-size: 82px;
    line-height: 80px;
    letter-spacing: 1px;
    text-shadow: 0 2px 6px rgba(0,0,0,0.15);
  }
  .tagline {
    position: absolute;
    right: 26px; top: 427px;
    width: 500px; height: 64px;
    background: var(--green);
    color: var(--white);
    font-weight: 600;
    font-size: 46px;
    letter-spacing: 5px;
    display: flex; align-items: center; justify-content: center;
  }
  .message {
    position: absolute;
    left: 155px; top: 725px;
    width: 744px; height: 182px;
    background: var(--green);
    border: 4px solid var(--white);
    border-radius: 22px;
    box-shadow: 0 6px 14px rgba(0,0,0,0.18);
    display: flex; align-items: center; justify-content: center;
    padding: 0 60px;
    color: var(--white);
    font-family: "Montserrat", sans-serif;
    font-weight: 700;
    font-size: 18.5px;
    line-height: 25px;
    text-align: center;
  }
  .cta {
    position: absolute;
    left: 413px; top: 951px;
    width: 228px; height: 58px;
    background: var(--blue);
    border-radius: 16px;
    color: var(--white);
    font-weight: 800;
    font-size: 26px;
    display: flex; align-items: center; justify-content: center;
  }
</style>
</head>
<body>
  <main class="post">
    <div class="brand">
      <span class="brand-mark"></span>
      <span class="brand-name">Brookvale Systems</span>
    </div>

    <div class="dots dots-top"><span></span><span></span><span></span><span></span><span></span><span></span><span></span><span></span><span></span></div>

    <svg class="hero" viewBox="0 0 1054 690" xmlns="http://www.w3.org/2000/svg" role="img" aria-label="Photo of a centre-pivot irrigation system spraying a green pasture beneath snow-capped mountains and blue sky">
      <defs>
        <linearGradient id="scene" x1="0" y1="0" x2="0" y2="1">
          <stop offset="0" stop-color="var(--sky-top)"/>
          <stop offset="0.45" stop-color="var(--sky-mid)"/>
          <stop offset="0.55" stop-color="var(--field-dark)"/>
          <stop offset="0.75" stop-color="var(--field)"/>
          <stop offset="1" stop-color="#b8c49a"/>
        </linearGradient>
      </defs>
      <polygon points="0,32 1054,12 1054,22 0,42" fill="var(--green)"/>
      <polygon points="0,38 1054,18 1054,660 0,660" fill="url(#scene)"/>
      <polygon points="0,658 1054,660 1054,676 0,682" fill="var(--green)"/>
    </svg>

    <h1 class="headline">WATER<br>CONSERVATION</h1>
    <div class="tagline">FOR BUSINESSES</div>

    <p class="message">Lorem ipsum dolor sit amet, consectetur adipiscing elit, sed do eiusmod tempor incididunt ut labore et dolore magna aliqua. Quis ipsum suspendisse ultrices gravida. Risus commodo viverra maecenas accumsan lacus vel facilisis.</p>

    <div class="dots dots-bottom"><span></span><span></span><span></span><span></span><span></span><span></span><span></span><span></span><span></span></div>

    <a class="cta">BOOK NOW</a>
  </main>
</body>
</html>
```